VORELLO - PIZZA - RESTAURANT PIZZERIA

Flyer format:
- A5 front / back leaflet (Example attachment)
Customer logos:
- Attachment, VORELLO PIZZA logo
Address and contact to put on the flyers:
- Phone to add: (+352) 26 58 40 71 (Page 1)
- Address to be added: 27 rue des tilleuls, L-3829 Kayl, Luxembourg (Page 1)
- Website: www.vorello-example.lu (Page 1)
- Leave a space for the timetable (last page)
Flyer color:
- Preferably black background with colored customer logo
Typefaces:
- At your convenience
Descriptions:
- We would like to have a flyer to the one we have put as an example in the attachment
Important elements:
- Pizza oven on the cover page with customer logo, address and contact details
- The graphic elements must be usable and non-paying, we want a quality visual.
- Menu (attachment) The menu is in Word format, it must be laid out in a thoughtful way as on the example model.
- We need to find some pizza and/or ingredient visuals
Aspects :
- The design of the set must be elegant, sober and must contain all the information (Menu, visual of your choice, logo)

Target Market(s)

Private and professional public

Font styles to use
Serif
Sans Serif

Requirements
Must have
• Elegance, take into account the information of the comment
Nice to have
• Pizza oven, Dominant color black, Gold, red
Should not have
• poor quality visuals

```html
<!DOCTYPE html>
<html lang="fr">
<head>
<meta charset="utf-8">
<title>Vorello Pizza – Pizza Menu Leaflet</title>
<link rel="stylesheet" href="https://fonts.googleapis.com/css2?family=Oswald:wght@500;700&family=PT+Sans+Narrow:wght@400&display=swap">
<style>
  :root {
    --backdrop: #e9e6e1;
    --night: #1d232b;
    --night-soft: #2c343e;
    --night-deep: #161b21;
    --gold: #e2b646;
    --gold-light: #f1cc62;
    --gold-dark: #b9892a;
    --ink: #2a2113;
    --paper-text: #f3f1ec;
  }
  * { box-sizing: border-box; margin: 0; padding: 0; }
  html, body { width: 1200px; height: 1200px; overflow: hidden; }
  body { background: var(--backdrop); position: relative; font-family: "PT Sans Narrow", sans-serif; }

  .leaflet-page {
    position: absolute; top: 264px; width: 476px; height: 672px; overflow: hidden;
    background: radial-gradient(ellipse at 50% 40%, var(--night-soft) 0%, var(--night) 55%, var(--night-deep) 100%);
  }
  .page-back { left: 109px; }
  .page-front { left: 615px; }

  .awning { position: absolute; top: 0; left: 0; width: 476px; height: 92px; display: block; }

  .menu-title {
    position: absolute; top: 108px; left: 0; width: 100%; text-align: center;
    font-family: "Oswald", sans-serif; font-weight: 700; font-size: 17px; color: #fff; letter-spacing: -0.2px;
  }
  .menu-columns { position: absolute; top: 134px; left: 52px; display: flex; gap: 21px; }
  .menu-column { width: 107px; list-style: none; }
  .menu-item {
    display: flex; align-items: baseline; height: 19.5px;
    font-size: 11.5px; color: var(--paper-text);
  }
  .menu-item .leader { flex: 1; border-bottom: 1px dotted var(--paper-text); margin: 0 2px; transform: translateY(-3px); }

  .photo-strip {
    position: absolute; top: 410px; left: 0; width: 100%; height: 118px;
    background: var(--night-deep); display: flex; gap: 5px; padding: 5px 0;
  }
  .photo { flex: 1; }
  .photo-one { background: linear-gradient(135deg, #5c3a1c, #c98a3a 50%, #7a4a20); }
  .photo-two { background: radial-gradient(circle at 45% 55%, #e8d6c2 0%, #d79a6a 45%, #2b4a5a 75%); }
  .photo-three { background: linear-gradient(120deg, #2a2a2e, #b9722e 45%, #e1b06a 70%, #3a2a20); }

  .brand-name {
    position: absolute; left: 0; width: 100%; text-align: center;
    font-family: "Oswald", sans-serif; font-weight: 500; color: var(--gold); letter-spacing: 4px;
  }
  .page-back .brand-name { top: 566px; font-size: 28px; }
  .page-front .brand-name { top: 162px; font-size: 44px; letter-spacing: 6px; }

  .menu-ribbon { position: absolute; top: 298px; left: 150px; width: 176px; height: 36px; display: block; }
  .menu-ribbon-label {
    position: absolute; top: 302px; left: 170px; width: 136px; text-align: center;
    font-family: "Oswald", sans-serif; font-weight: 700; font-size: 17px; color: var(--ink);
  }

  .hero-pizza {
    position: absolute; top: 432px; left: 0; width: 100%; height: 214px;
    background: radial-gradient(ellipse 70% 60% at 50% 50%, #e0a13a 0%, #cf5a28 45%, #a3431e 65%, #3b2a20 90%, var(--night-deep) 100%);
  }

  .contact-bar {
    position: absolute; bottom: 0; left: 0; width: 100%; height: 26px;
    background: linear-gradient(var(--gold-light), var(--gold));
    color: var(--ink); font-size: 11px; text-align: center; line-height: 26px; white-space: nowrap;
  }
</style>
</head>
<body>
<svg width="0" height="0" style="position:absolute">
  <defs>
    <linearGradient id="stripe-gold" x1="0" x2="1" y1="0" y2="0">
      <stop offset="0" stop-color="#c99a2e"/>
      <stop offset="0.5" stop-color="#f1cc62"/>
      <stop offset="1" stop-color="#d7a93c"/>
    </linearGradient>
    <g id="awning-tabs">
      <rect x="0" y="0" width="476" height="70" fill="#b9892a"/>
      <path d="M0 0h41v72a20.5 20.5 0 0 1-41 0z" fill="url(#stripe-gold)"/>
      <path d="M41 0h41v72a20.5 20.5 0 0 1-41 0z" fill="url(#stripe-gold)"/>
      <path d="M82 0h41v72a20.5 20.5 0 0 1-41 0z" fill="url(#stripe-gold)"/>
      <path d="M123 0h41v72a20.5 20.5 0 0 1-41 0z" fill="url(#stripe-gold)"/>
      <path d="M164 0h41v72a20.5 20.5 0 0 1-41 0z" fill="url(#stripe-gold)"/>
      <path d="M205 0h41v72a20.5 20.5 0 0 1-41 0z" fill="url(#stripe-gold)"/>
      <path d="M246 0h41v72a20.5 20.5 0 0 1-41 0z" fill="url(#stripe-gold)"/>
      <path d="M287 0h41v72a20.5 20.5 0 0 1-41 0z" fill="url(#stripe-gold)"/>
      <path d="M328 0h41v72a20.5 20.5 0 0 1-41 0z" fill="url(#stripe-gold)"/>
      <path d="M369 0h41v72a20.5 20.5 0 0 1-41 0z" fill="url(#stripe-gold)"/>
      <path d="M410 0h41v72a20.5 20.5 0 0 1-41 0z" fill="url(#stripe-gold)"/>
      <path d="M451 0h41v72a20.5 20.5 0 0 1-41 0z" fill="url(#stripe-gold)"/>
    </g>
  </defs>
</svg>

<section class="leaflet-page page-back" aria-label="Verso : carte des suppléments">
  <svg class="awning" viewBox="0 0 476 92"><use href="#awning-tabs"/></svg>

  <h2 class="menu-title">FROMAGES: VIANDES: LEGUMES:</h2>

  <div class="menu-columns">
    <ul class="menu-column">
      <li class="menu-item">mozza<span class="leader"></span>1,50€</li>
      <li class="menu-item">burrata<span class="leader"></span>3,50€</li>
      <li class="menu-item">buffala<span class="leader"></span>5€</li>
      <li class="menu-item">câpre<span class="leader"></span>1,50€</li>
      <li class="menu-item">pomme de terre<span class="leader"></span>2€</li>
      <li class="menu-item">lardon<span class="leader"></span>2€</li>
      <li class="menu-item">gorgonzola<span class="leader"></span>2€</li>
      <li class="menu-item">anchois<span class="leader"></span>1,50€</li>
      <li class="menu-item">courgette<span class="leader"></span>2€</li>
      <li class="menu-item">saumon<span class="leader"></span>3,50€</li>
      <li class="menu-item">chorizo<span class="leader"></span>2,50€</li>
      <li class="menu-item">fruit de mer<span class="leader"></span>3,50€</li>
      <li class="menu-item">jambon cru<span class="leader"></span>2€</li>
    </ul>
    <ul class="menu-column">
      <li class="menu-item">poulet<span class="leader"></span>2,50€</li>
      <li class="menu-item">viande hachee<span class="leader"></span>2,50€</li>
      <li class="menu-item">merguez<span class="leader"></span>2,50€</li>
      <li class="menu-item">chevre<span class="leader"></span>2€</li>
      <li class="menu-item">ail<span class="leader"></span>1€</li>
      <li class="menu-item">aubergine<span class="leader"></span>2€</li>
      <li class="menu-item">jambon de parme<span class="leader"></span>3,50€</li>
      <li class="menu-item">parmesan<span class="leader"></span>2,50€</li>
      <li class="menu-item">œuf<span class="leader"></span>1€</li>
      <li class="menu-item">roquette<span class="leader"></span>2€</li>
      <li class="menu-item">tomate cerise<span class="leader"></span>2€</li>
      <li class="menu-item">scampi<span class="leader"></span>3,50€</li>
    </ul>
    <ul class="menu-column">
      <li class="menu-item">poivron<span class="leader"></span>1,50€</li>
      <li class="menu-item">champignon<span class="leader"></span>2€</li>
      <li class="menu-item">oignon<span class="leader"></span>1,50€</li>
      <li class="menu-item">jambon cuit<span class="leader"></span>2€</li>
      <li class="menu-item">st nectaire<span class="leader"></span>2,50€</li>
      <li class="menu-item">olive<span class="leader"></span>1€</li>
      <li class="menu-item">artichaud<span class="leader"></span>1,50€</li>
      <li class="menu-item">thon<span class="leader"></span>2€</li>
      <li class="menu-item">ricotta<span class="leader"></span>2€</li>
      <li class="menu-item">Ananas<span class="leader"></span>2€</li>
      <li class="menu-item">pistache<span class="leader"></span>1€</li>
      <li class="menu-item">andouillette<span class="leader"></span>2€</li>
    </ul>
  </div>

  <div class="photo-strip">
    <div class="photo photo-one" role="img" aria-label="Photo d'une pizza gratinée en plat"></div>
    <div class="photo photo-two" role="img" aria-label="Photo d'une pizza aux poivrons et oignons"></div>
    <div class="photo photo-three" role="img" aria-label="Photo de parts de pizza au fromage"></div>
  </div>

  <p class="brand-name">VORELLO PIZZA</p>

  <footer class="contact-bar">add: 27 rue des tilleuls, L-3829 Kayl, Luxembourg | Ph : (+352) 26 58 40 71 | www.vorello-example.lu</footer>
</section>

<section class="leaflet-page page-front" aria-label="Recto : couverture">
  <svg class="awning" viewBox="0 0 476 92"><use href="#awning-tabs"/></svg>

  <h1 class="brand-name">VORELLO PIZZA</h1>

  <svg class="menu-ribbon" viewBox="0 0 176 36">
    <path d="M0 6h28v22H0l8-11z" fill="var(--gold-dark)"/>
    <path d="M176 6h-28v22h28l-8-11z" fill="var(--gold-dark)"/>
    <rect x="20" y="2" width="136" height="28" fill="var(--gold)"/>
    <rect x="20" y="30" width="136" height="2" fill="#8a651c"/>
  </svg>
  <p class="menu-ribbon-label">PIZZA MENU</p>

  <div class="hero-pizza" role="img" aria-label="Photo d'une pizza aux tomates cerises, mozzarella et basilic"></div>

  <footer class="contact-bar">add: 27 rue des tilleuls, L-3829 Kayl, Luxembourg | Ph : (+352) 26 58 40 71 | www.vorello-example.lu</footer>
</section>
</body>
</html>
```